Home page design for Drone video business (the Business focusses on home videos for realtors)

Dear reader,

*I NEED DESIGNS OF ALL THE PAGES*
We need a first design of a homepage and of 4 other pages of the website of a business that sells drone video services. All the pages will need to be in the similar design style.
The video's are targeted at consumers that want to sell there home and would like to have a cool drone video of photos of their home.

How does the website look:
- has a navbar on top
- A cool looking banner of an areal drone.
- A Big header: with company name: SkyNestReels
- A smaller subheader: We film your home to increase your chances of sale
- Then a section with a Big header: How does it work
- In this section a place for a vimeo explainitory video
- Then a similar navbar styled bar with a phone number and a email address
- Then a section where the videos porfolio is displayed in a cool way
- Inside this sectiona header: Our work

- A section with header: Why us?
- 4 symbols here with a subheader and some lorum ipsum text underneath (see wireframe images)

- Under that a: Contact us
- where you can put in name, email, phone, message box and a send button

- At the bottom a footer with phone number and a fake address for now.

Be creative. Use creative but serious color.
Use a serious font. Make it a sharp design. Sharp lines. Not to dark design and not to light design.

The wireframes are the same kind of images.
PLEASE PUT IN DESIGNS OF ALL THE PAGES

Good luck

Target Market(s)

People that want to sell home and want to make a cool drone video or photos of their home.

Industry/Entity Type

Business

Contact Information for Business Card

Milo Brenning
milo@skynestreels.example
+31647283915

Logo Text

SkyNestReels

Number of Pages Required

1 page

Font styles to use
Sans Serif

Requirements
Must have
• All the sections as explained in the instructions.
• The nav bar should have an about us, services, portfolio and a contact us buttons.
• See instruction for details.
• Must include designs of the front page, contact us, our services, portfolio and contact us.
• If you do add some designs for the "about us", "services", "prices", "portfolio" and "contact us" pages, you make a way better chance of winning the competition.
Nice to have
• designs for the other pages as described at the Must haves. You make a better chance of winning if you include them. Look at the wireframes to see the mockups for those pages. think creative about what kind of sections and design should be included in those pages.
Should not have
• bad designs.

```html
<!DOCTYPE html>
<html lang="en">
<head>
<meta charset="utf-8">
<title>SkyNestReels – Home</title>
<link rel="stylesheet" href="https://fonts.googleapis.com/css2?family=Arimo:wght@400;700&display=swap">
<style>
:root{
  --bar:#3a3837;
  --teal:#4dbfcc;
  --ink:#111111;
  --body:#6b6b6b;
  --white:#ffffff;
  --band:#e4e4e4;
  --field-line:#cfcfcf;
  --placeholder:#a9a9a9;
  --video:#000000;
  --player:#d9d9d9;
  --icon-bg:#e3e3e3;
  --gold:#f2b705;
  --leaf:#1f7a3a;
  --chart:#3f9b2f;
}
*{margin:0;padding:0;box-sizing:border-box}
html,body{width:1200px;height:3000px;overflow:hidden;background:var(--white)}
body{position:relative;font-family:"Arimo",Arial,sans-serif;color:var(--ink)}
.abs{position:absolute}

/* navigation */
.site-nav{left:0;top:0;width:1200px;height:96px;background:var(--bar)}
.brand{left:0;top:0;width:182px;height:96px;background:var(--teal);color:var(--white);font-size:56px;line-height:96px;padding-left:22px}
.nav-link{top:36px;color:var(--white);font-size:17px}

/* hero */
.hero{left:0;top:96px;width:1200px;height:498px;
  background:
    radial-gradient(ellipse 160px 300px at 40px 120px,rgba(48,62,40,.95),rgba(48,62,40,0) 100%),
    radial-gradient(ellipse 200px 220px at 60px 470px,rgba(60,70,48,.9),rgba(60,70,48,0) 100%),
    radial-gradient(ellipse 260px 120px at 300px 40px,rgba(70,88,60,.7),rgba(70,88,60,0) 100%),
    radial-gradient(ellipse 200px 320px at 1200px 300px,rgba(90,100,96,.55),rgba(90,100,96,0) 100%),
    radial-gradient(ellipse 420px 90px at 700px 120px,rgba(240,244,248,.75),rgba(240,244,248,0) 100%),
    radial-gradient(ellipse 380px 80px at 820px 420px,rgba(232,238,244,.7),rgba(232,238,244,0) 100%),
    radial-gradient(ellipse 170px 130px at 360px 230px,rgba(245,245,245,.6),rgba(245,245,245,0) 100%),
    linear-gradient(180deg,#93b3d3 0%,#b5cbe0 55%,#c9d7e4 100%)}
.hero-title{left:440px;width:700px;top:344px;text-align:center;color:var(--white);font-size:50px;font-weight:400;text-shadow:2px 2px 3px rgba(0,0,0,.55)}
.hero-sub{left:430px;width:700px;top:402px;text-align:center;color:var(--white);font-size:35px;line-height:46px;font-weight:700;text-shadow:2px 2px 3px rgba(0,0,0,.55)}

/* section headings */
.section-title{left:0;width:1200px;text-align:center;font-size:42px;font-weight:400;color:var(--ink)}

/* explainer video */
.explainer{left:24px;top:690px;width:1152px;height:378px;background:var(--video)}
.player-bar{left:24px;top:1040px;width:1152px;height:28px;background:var(--player)}
.player-time{left:128px;top:1046px;font-size:13px;color:#333}

/* contact strip */
.contact-icon{width:80px;height:80px;border-radius:50%;background:var(--ink)}
.contact-text{font-size:27px;color:#333}

/* works */
.works-band{left:0;top:1270px;width:1200px;height:296px;background:var(--band)}
.work-thumb{top:1312px;width:324px;height:208px;background:var(--video)}
.work-bar{top:1506px;width:324px;height:14px;background:var(--player)}
.slider-arrow{top:1402px;width:44px;height:44px;border-radius:50%;background:#bdbdbd}

/* features */
.feature-icon{width:144px;height:144px;border-radius:50%;background:var(--icon-bg)}
.feature-title{width:520px;text-align:center;font-size:38px;font-weight:400;color:#444}
.feature-text{width:520px;text-align:center;font-size:16px;line-height:22px;color:var(--body);white-space:nowrap}

/* form */
.field{border:1px solid var(--field-line);background:var(--white);color:var(--placeholder);font-size:20px;padding:18px 16px}
.submit-btn{left:24px;top:2712px;width:188px;height:62px;border:1px solid var(--field-line);background:linear-gradient(#f7f7f7,#e6e6e6);color:var(--placeholder);font-size:24px;text-align:center;line-height:60px}

/* footer */
.site-footer{left:0;top:2810px;width:1200px;height:190px;background:var(--bar)}
.social{top:2856px;width:66px;height:66px;border-radius:50%;border:3px solid var(--white);color:var(--white);font-size:11px;font-weight:700;text-align:center;line-height:60px}
.footer-links{left:400px;width:400px;top:2880px;text-align:center;color:var(--white);font-size:14px;font-weight:700;line-height:18px}
.footer-phone{left:974px;top:2840px;color:var(--white);font-size:28px;font-weight:700}
.footer-address{right:24px;top:2884px;text-align:right;color:var(--white);font-size:24px;line-height:32px}
</style>
</head>
<body>

<header class="abs site-nav">
  <div class="abs brand">SNR</div>
  <span class="abs nav-link" style="left:726px">Services</span>
  <span class="abs nav-link" style="left:848px">About Us</span>
  <span class="abs nav-link" style="left:970px">Portfolios</span>
  <span class="abs nav-link" style="left:1104px">Contacts</span>
</header>

<section class="abs hero" role="img" aria-label="Photo of a white camera drone hovering in a blue sky beside tree branches"></section>
<h1 class="abs hero-title">SKYNESTREELS</h1>
<p class="abs hero-sub">we film your home to increase<br>your chances of sale</p>

<h2 class="abs section-title" style="top:620px">HOW DOES IT WORK?</h2>
<div class="abs explainer"></div>
<svg class="abs" style="left:550px;top:820px" width="100" height="76" viewBox="0 0 100 76">
  <rect width="100" height="76" rx="12" fill="#2b2b2b"/>
  <path d="M40 22 L64 38 L40 54 Z" fill="#ffffff"/>
</svg>
<div class="abs player-bar"></div>
<svg class="abs" style="left:44px;top:1046px" width="70" height="16" viewBox="0 0 70 16">
  <path d="M2 2 L12 8 L2 14 Z" fill="#333"/>
  <path d="M44 5 h4 l5 -4 v14 l-5 -4 h-4 Z" fill="#333"/>
</svg>
<span class="abs player-time">0:00 / 2:20</span>

<svg class="abs contact-icon" style="left:210px;top:1104px" viewBox="0 0 80 80">
  <circle cx="40" cy="40" r="40" fill="#111"/>
  <path d="M28 20 c-4 2 -6 6 -4 12 c4 12 12 22 24 28 c6 2 10 0 12 -4 l-7 -7 c-2 -1 -4 0 -5 2 c-6 -3 -11 -9 -13 -15 c2 -1 3 -3 2 -5 Z" fill="#fff"/>
</svg>
<span class="abs contact-text" style="left:320px;top:1128px">+31652804417</span>
<svg class="abs contact-icon" style="left:644px;top:1102px" viewBox="0 0 80 80">
  <circle cx="40" cy="40" r="40" fill="#111"/>
  <rect x="20" y="26" width="40" height="28" fill="#fff"/>
  <path d="M20 26 L40 42 L60 26 M20 54 L34 40 M60 54 L46 40" stroke="#111" stroke-width="2.5" fill="none"/>
</svg>
<span class="abs contact-text" style="left:770px;top:1124px">contact@skynestreels.example</span>

<h2 class="abs section-title" style="top:1202px">OUR WORKS</h2>
<section class="abs works-band"></section>
<div class="abs slider-arrow" style="left:26px"></div>
<svg class="abs" style="left:26px;top:1402px" width="44" height="44" viewBox="0 0 44 44"><path d="M25 13 L16 22 L25 31" stroke="#fff" stroke-width="4" fill="none"/></svg>
<div class="abs slider-arrow" style="left:1128px"></div>
<svg class="abs" style="left:1128px;top:1402px" width="44" height="44" viewBox="0 0 44 44"><path d="M19 13 L28 22 L19 31" stroke="#fff" stroke-width="4" fill="none"/></svg>

<div class="abs work-thumb" style="left:92px"></div>
<div class="abs work-bar" style="left:92px"></div>
<div class="abs work-thumb" style="left:438px"></div>
<div class="abs work-bar" style="left:438px"></div>
<div class="abs work-thumb" style="left:782px"></div>
<div class="abs work-bar" style="left:782px"></div>
<svg class="abs" style="left:234px;top:1398px" width="40" height="32" viewBox="0 0 40 32"><rect width="40" height="32" rx="6" fill="#2b2b2b"/><path d="M16 9 L26 16 L16 23 Z" fill="#fff"/></svg>
<svg class="abs" style="left:580px;top:1398px" width="40" height="32" viewBox="0 0 40 32"><rect width="40" height="32" rx="6" fill="#2b2b2b"/><path d="M16 9 L26 16 L16 23 Z" fill="#fff"/></svg>
<svg class="abs" style="left:924px;top:1398px" width="40" height="32" viewBox="0 0 40 32"><rect width="40" height="32" rx="6" fill="#2b2b2b"/><path d="M16 9 L26 16 L16 23 Z" fill="#fff"/></svg>

<h2 class="abs section-title" style="top:1596px">WHY US?</h2>

<!-- feature: price -->
<svg class="abs feature-icon" style="left:212px;top:1670px" viewBox="0 0 144 144" role="img" aria-label="Gold dollar sign icon for low prices">
  <circle cx="72" cy="72" r="72" fill="#e3e3e3"/>
  <text x="72" y="100" text-anchor="middle" font-family="Arimo, Arial, sans-serif" font-weight="700" font-size="82" fill="#f2b705">$</text>
</svg>
<h3 class="abs feature-title" style="left:22px;top:1816px">Cheap</h3>
<p class="abs feature-text" style="left:22px;top:1870px">Lorem ipsum dolor sit amet, consectetuer adipiscing elit.<br>Aenean commodo ligula eget dolor. Aenean massa. Cum<br>sociis natoque penatibus et magnis dis parturient montes,<br>nascetur ridiculus mus. Donec quam felis, ultricies nec,</p>

<!-- feature: flexibility -->
<svg class="abs feature-icon" style="left:822px;top:1670px" viewBox="0 0 144 144" role="img" aria-label="Green leaf icon for flexibility">
  <circle cx="72" cy="72" r="72" fill="#e3e3e3"/>
  <path d="M66 114 C44 96 46 60 70 30 C86 56 88 92 66 114 Z" fill="#1f7a3a"/>
  <path d="M72 116 C78 96 92 84 104 80 C104 98 92 112 72 116 Z" fill="#2f9a4a"/>
  <path d="M66 112 C64 90 66 62 70 36" stroke="#e3e3e3" stroke-width="2" fill="none"/>
</svg>
<h3 class="abs feature-title" style="left:632px;top:1816px">Flexible</h3>
<p class="abs feature-text" style="left:632px;top:1870px">Lorem ipsum dolor sit amet, consectetuer adipiscing elit.<br>Aenean commodo ligula eget dolor. Aenean massa. Cum<br>sociis natoque penatibus et magnis dis parturient montes,<br>nascetur ridiculus mus. Donec quam felis, ultricies nec,</p>

<!-- feature: equality -->
<div class="abs feature-icon" style="left:210px;top:1970px;background:radial-gradient(ellipse 44px 30px at 72px 76px,#8a8a8a 0%,#c4c4c4 60%,#e3e3e3 100%)" role="img" aria-label="Icon of two figures shaking hands for equality"></div>
<h3 class="abs feature-title" style="left:22px;top:2120px">Equality</h3>
<p class="abs feature-text" style="left:22px;top:2174px">Lorem ipsum dolor sit amet, consectetuer adipiscing elit.<br>Aenean commodo ligula eget dolor. Aenean massa. Cum<br>sociis natoque penatibus et magnis dis parturient montes,<br>nascetur ridiculus mus. Donec quam felis, ultricies nec,</p>

<!-- feature: sales chart -->
<svg class="abs feature-icon" style="left:822px;top:1970px" viewBox="0 0 144 144" role="img" aria-label="Rising green sales chart icon">
  <circle cx="72" cy="72" r="72" fill="#e3e3e3"/>
  <rect x="34" y="92" width="10" height="12" fill="#bdbdbd"/>
  <rect x="50" y="86" width="10" height="18" fill="#bdbdbd"/>
  <rect x="66" y="78" width="10" height="26" fill="#bdbdbd"/>
  <rect x="82" y="68" width="10" height="36" fill="#bdbdbd"/>
  <rect x="98" y="56" width="10" height="48" fill="#bdbdbd"/>
  <path d="M30 92 L52 80 L66 84 L86 62 L104 50" stroke="#3f9b2f" stroke-width="5" fill="none" stroke-linejoin="round"/>
  <path d="M96 44 L112 42 L108 58 Z" fill="#3f9b2f"/>
</svg>
<h3 class="abs feature-title" style="left:632px;top:2118px">Increase Sales</h3>
<p class="abs feature-text" style="left:632px;top:2174px">Lorem ipsum dolor sit amet, consectetuer adipiscing elit.<br>Aenean commodo ligula eget dolor. Aenean massa. Cum<br>sociis natoque penatibus et magnis dis parturient montes,<br>nascetur ridiculus mus. Donec quam felis, ultricies nec,</p>

<h2 class="abs section-title" style="top:2302px">CONTACT US</h2>
<div class="abs field" style="left:22px;top:2372px;width:380px;height:62px">Name</div>
<div class="abs field" style="left:412px;top:2372px;width:368px;height:62px">Email</div>
<div class="abs field" style="left:802px;top:2372px;width:374px;height:62px;padding-left:40px">Phone no</div>
<div class="abs field" style="left:22px;top:2442px;width:1154px;height:258px">Full Message Here</div>
<div class="abs submit-btn">Submit</div>

<footer class="abs site-footer"></footer>
<div class="abs social" style="left:24px">Nook</div>
<div class="abs social" style="left:114px">Chirp</div>
<div class="abs social" style="left:202px">Snapgrid</div>
<p class="abs footer-links">Home | Privacy &amp; Policy | Terms &amp; Condition<br>Copyright all right reserved by SNR</p>
<svg class="abs" style="left:922px;top:2836px" width="36" height="40" viewBox="0 0 36 40">
  <path d="M8 2 c-5 2 -7 7 -5 14 c4 11 11 19 21 23 c5 1 8 -1 10 -4 l-7 -7 c-2 -1 -4 0 -5 2 c-5 -3 -9 -8 -11 -14 c2 -1 3 -3 2 -5 Z" fill="#fff"/>
</svg>
<span class="abs footer-phone">+31652804417</span>
<p class="abs footer-address">31 Address Line one<br>south point, Au</p>

</body>
</html>
```